New Website for Crime Scene Cleaner required

I need someone to create a complete new website and can set up SEO for me through the Website Designer or a third party for me. I have Logo that i will upload shortly once finalized for the website. I have domain names already but will need to be registered by the winner(i can supply the details I have received from NetHarbor). I am looking for a website that stands out but is simple and elegant, easy to navigate and use yet not boring. Using information provided by me for wording to create it as a stand out website. in total i am looking at 5-7 pages (About/Home, Fire & Smoke Restoration, Water Restoration/Mould Remediation, Crime Scene Cleaners, Methamphetamine Remediation/ Testing Services, Hoarding & Squalor Cleaning, Contact Us/Testimonials)This will be a start to finish project. I would like assistance to have it set up user friendly on mobile devices etc or refer a third party who can assist. Must be able to provide ongoing support when required by myself if the successful winner (i understand this will be an additional fee if required in the future).
You will also require to assist me with the email set up for the website so that it is fully functional or provide a third party who can.
To gain some information about the business you can visit my old website at www.pelgrosvandree.com.au and welcome to use some of the wording from there for your entry.
It's been 14yrs since i've had a website made from me so suggestions are welcome if not mentioned in the scope as I want the website to be great.

I have uploaded 2 Logo's and a 3D Logo will come through shortly.

Target Market(s)

People affected by a traumatic event in their lives needing assistance by professionals who are understanding and professionally trained

Coding

Coded - Design and coding required

Requirements
Must have
• *** Please note that correct wording for pages will only be supplied upon a successful winner for the finalization of the project.

I have domain names already but will need to be registered by the winner(i can supply the details I have received from NetHarbor).
Nice to have
• the feeling that we care because we do and that we are passionate for what we do.

```html
<!DOCTYPE html>
<html lang="en">
<head>
<meta charset="utf-8">
<title>Haven &amp; Restore Services</title>
<link href="https://fonts.googleapis.com/css2?family=Lato:ital,wght@0,400;0,700;0,900;1,400;1,700&display=swap" rel="stylesheet">
<style>
:root{
  --red:#e2351f;
  --orange:#f26a1b;
  --ink:#1d1d1d;
  --text:#333;
  --grey-bg:#f0f0f0;
  --footer:#2b2b2b;
  --white:#fff;
}
*{margin:0;padding:0;box-sizing:border-box}
html,body{width:1200px;height:3895px;overflow:hidden}
body{position:relative;font-family:'Lato',sans-serif;color:var(--text);background:var(--white)}
.abs{position:absolute}
a{color:inherit;text-decoration:none}

/* header */
.brand{left:75px;top:44px;width:320px}
.brand-name{display:flex;align-items:center;gap:10px;font-weight:900;font-size:23px;color:var(--red);letter-spacing:.5px;white-space:nowrap}
.brand-name .dot{width:22px;height:22px;border-radius:50%;background:var(--orange);flex:none}
.brand-sub{font-size:12px;font-weight:700;letter-spacing:4px;color:var(--ink);margin:6px 0 0 32px}
.top-contact{right:75px;top:56px;display:flex;gap:24px;font-size:19px;font-weight:700;color:var(--ink);white-space:nowrap}
.top-contact span{display:flex;align-items:center;gap:10px}

/* nav */
.nav{left:0;top:140px;width:1200px;height:58px;background:var(--red);display:flex;justify-content:center;align-items:center;gap:29px}
.nav a{color:var(--white);font-size:12px;font-weight:700;letter-spacing:.2px;white-space:nowrap}

/* hero */
.hero{left:0;top:198px;width:1200px;height:512px;background:linear-gradient(160deg,#2e4a7c 0%,#6b7c95 35%,#3a3430 70%,#1e1a18 100%)}
.hero-title{left:0;top:405px;width:1200px;text-align:center;font-size:80px;font-weight:900;color:var(--white);text-shadow:0 3px 8px rgba(0,0,0,.5);white-space:nowrap}
.dots{left:558px;top:655px;display:flex;gap:13px}
.dots i{width:12px;height:12px;border-radius:50%;background:var(--white)}
.dots i:first-child{background:var(--red)}

/* about */
h2{font-weight:900;color:var(--ink);font-size:35px;white-space:nowrap}
.lead{color:var(--red);font-size:21px;line-height:28px}
.about-h{left:75px;top:782px}
.about-lead{left:75px;top:843px;width:590px}
.about-p{left:75px;top:912px;font-size:16px}
.about-em{left:75px;top:948px;font-size:15px;font-style:italic;font-weight:700;line-height:26px;color:#222}
.checks{list-style:none;font-size:14.5px}
.checks li{display:flex;align-items:center;gap:18px;height:32px;white-space:nowrap}
.about-list{left:75px;top:1011px}
.btn{display:flex;align-items:center;justify-content:center;background:var(--ink);color:var(--white);border-radius:24px;font-weight:900;font-size:17px;height:46px;width:178px}
.about-btn{left:75px;top:1213px}
.frame-back{background:var(--orange)}
.photo-a{left:673px;top:800px;width:444px;height:458px;background:linear-gradient(135deg,#e9e9e9,#b8c0cc 45%,#6e6a5a 80%,#c8b420)}

/* services */
.svc-bg{left:0;top:1325px}
.svc-h{left:0;top:1477px;width:1200px;text-align:center}
.svc-item h3{color:var(--orange);font-size:16.5px;font-weight:900;margin-bottom:8px;white-space:nowrap}
.svc-item p{font-size:14px;line-height:26px}
.right{text-align:right}
.center-name{left:440px;top:1757px;width:320px;text-align:center;font-size:30px;font-weight:900;color:var(--red);white-space:nowrap}

/* crime */
.photo-b{left:84px;top:2311px;width:444px;height:459px;background:linear-gradient(135deg,#8c8c8c,#d0d0d0 40%,#2a2e33 70%,#555)}
.crime-h{left:566px;top:2298px}
.crime-lead{left:566px;top:2356px;width:570px}
.crime-list{left:566px;top:2423px;display:grid;grid-template-columns:232px 240px;font-size:14.5px}
.crime-list li{height:39.5px}
.crime-p{left:566px;top:2546px;width:530px;font-size:14px;line-height:26px}
.crime-btn{left:566px;top:2723px}

/* testimonials */
.testi-bg{left:0;top:2830px}
.testi-h{left:0;top:2955px;width:1200px;text-align:center;color:var(--white);font-size:34px;font-weight:900}
.quote{top:3030px;width:320px;text-align:center;color:var(--white)}
.quote .q{width:52px;height:52px;border-radius:50%;background:var(--ink);margin:0 auto 22px;display:flex;align-items:center;justify-content:center;font-size:44px;font-weight:900;line-height:1;padding-top:16px}
.quote p{font-size:14.5px;line-height:26.5px}
.quote b{display:block;margin-top:16px;font-size:14.5px;font-weight:900;color:var(--ink)}
.arrow{top:3152px}

/* contact */
.touch-h{left:0;top:3480px;width:1200px;text-align:center}
.touch-c{left:0;top:3548px;width:1200px;display:flex;justify-content:center;gap:24px;color:var(--red);font-size:21px;font-weight:700;white-space:nowrap}
.touch-c span{display:flex;align-items:center;gap:12px}
.touch-btn{left:511px;top:3614px}

/* footer */
.footer{left:0;top:3718px;width:1200px;height:177px;background:var(--footer)}
.fnav{left:0;top:3762px;width:1200px;display:flex;justify-content:center;gap:31px;color:var(--white);font-size:11px;font-weight:700;white-space:nowrap}
.copy{left:0;top:3794px;width:1200px;text-align:center;color:var(--white);font-size:12px}
.social{left:526px;top:3825px;display:flex;gap:26px}
.social i{width:18px;height:18px;border-radius:50%;background:var(--white)}
</style>
</head>
<body>

<header>
  <div class="abs brand">
    <div class="brand-name"><span class="dot"></span>HAVEN &amp; RESTORE</div>
    <div class="brand-sub">SERVICES</div>
  </div>
  <div class="abs top-contact">
    <span><svg width="18" height="18" viewBox="0 0 24 24"><path fill="#e2351f" d="M6.6 10.8a15.1 15.1 0 0 0 6.6 6.6l2.2-2.2c.3-.3.7-.4 1-.2 1.1.4 2.3.6 3.6.6.6 0 1 .4 1 1V20c0 .6-.4 1-1 1A17 17 0 0 1 3 4c0-.6.4-1 1-1h3.5c.6 0 1 .4 1 1 0 1.3.2 2.5.6 3.6.1.3 0 .7-.2 1z"/></svg>1-800-555-0142</span>
    <span><svg width="20" height="16" viewBox="0 0 24 18"><path fill="#e2351f" d="M0 2l12 8 12-8V0H0zm0 3v13h24V5l-12 8z"/></svg>hello@havenrestore.example</span>
  </div>
</header>

<nav class="abs nav">
  <a>HOME</a><a>FIRE &amp; SMOKE RESTORATION</a><a>WATER RESTORATION</a><a>CRIME SCENE CLEANERS</a><a>TESTING SERVICES</a><a>HOARDING &amp; SQUALOR CLEANING</a><a>CONTACT US</a>
</nav>

<section>
  <div class="abs hero" role="img" aria-label="Photo of cleaners in white protective suits clearing fire-damaged debris"></div>
  <h1 class="abs hero-title">HAVEN &amp; RESTORE</h1>
  <div class="abs dots"><i></i><i></i><i></i><i></i></div>
</section>

<section>
  <h2 class="abs about-h">ABOUT HAVEN &amp; RESTORE</h2>
  <p class="abs lead about-lead">Haven &amp; Restore specialises in all Forensic &amp; Trauma Cleaning, Domestic and Commercial cleaning.</p>
  <p class="abs about-p">Haven &amp; Restore services the Southeast QLD Region.</p>
  <p class="abs about-em">Haven &amp; Restore has a team of experienced and quality driven cleaners,<br>we pride ourselves on:</p>
  <ul class="abs checks about-list">
    <li><svg width="14" height="14" viewBox="0 0 14 14"><circle cx="7" cy="7" r="7" fill="#e2351f"/><path d="M4 7.2l2 2 4-4" stroke="#fff" stroke-width="2" fill="none"/></svg>Providing the best clean</li>
    <li><svg width="14" height="14" viewBox="0 0 14 14"><circle cx="7" cy="7" r="7" fill="#e2351f"/><path d="M4 7.2l2 2 4-4" stroke="#fff" stroke-width="2" fill="none"/></svg>Attention to detail</li>
    <li><svg width="14" height="14" viewBox="0 0 14 14"><circle cx="7" cy="7" r="7" fill="#e2351f"/><path d="M4 7.2l2 2 4-4" stroke="#fff" stroke-width="2" fill="none"/></svg>Customer satisfaction</li>
    <li><svg width="14" height="14" viewBox="0 0 14 14"><circle cx="7" cy="7" r="7" fill="#e2351f"/><path d="M4 7.2l2 2 4-4" stroke="#fff" stroke-width="2" fill="none"/></svg>Friendly service and listening to the needs of our customers</li>
    <li><svg width="14" height="14" viewBox="0 0 14 14"><circle cx="7" cy="7" r="7" fill="#e2351f"/><path d="M4 7.2l2 2 4-4" stroke="#fff" stroke-width="2" fill="none"/></svg>A competitive price for the best quality service</li>
  </ul>
  <a class="abs btn about-btn">READ MORE</a>
  <div class="abs frame-back" style="left:683px;top:790px;width:444px;height:465px"></div>
  <div class="abs photo-a" role="img" aria-label="Photo of a technician in a protective suit spraying disinfectant on a stairway"></div>
</section>

<section>
  <svg class="abs svc-bg" width="1200" height="910" viewBox="0 0 1200 910">
    <path d="M0 50 C200 -20 600 -20 1200 265 L1200 740 C900 930 300 900 0 650 Z" fill="#f0f0f0"/>
    <g fill="none" stroke="#f26a1b" stroke-width="2">
      <polyline points="522,271 603,271 603,333"/>
      <polyline points="780,416 830,416"/>
      <polyline points="375,498 425,498"/>
      <polyline points="603,572 603,636 673,636"/>
      <path d="M460 420 A175 125 0 0 1 600 320" stroke-width="4"/>
      <path d="M740 390 A175 125 0 0 1 760 470" stroke-width="4"/>
      <path d="M440 480 A175 125 0 0 0 560 570" stroke-width="4"/>
    </g>
    <ellipse cx="602" cy="452" rx="170" ry="118" fill="#fff" transform="rotate(-18 602 452)"/>
    <g transform="rotate(-18 463 271)"><ellipse cx="463" cy="271" rx="62" ry="38" fill="#1d1d1d" stroke="#f26a1b" stroke-width="3"/></g>
    <g fill="none" stroke="#fff" stroke-width="2"><rect x="446" y="253" width="30" height="36"/><path d="M452 262h6M463 262h6M452 272h6M463 272h6"/></g>
    <g transform="rotate(-18 884 416)"><ellipse cx="884" cy="416" rx="62" ry="38" fill="#fff" stroke="#f26a1b" stroke-width="3"/></g>
    <g fill="none" stroke="#1d1d1d" stroke-width="2"><path d="M872 403l8-5 8 5v9l-8 5-8-5z"/><path d="M888 416l8-5 8 5v9l-8 5-8-5z"/></g>
    <g transform="rotate(-18 311 498)"><ellipse cx="311" cy="498" rx="62" ry="38" fill="#fff" stroke="#f26a1b" stroke-width="3"/></g>
    <g fill="none" stroke="#1d1d1d" stroke-width="2"><path d="M294 498l17-15 17 15M298 495v15h26v-15M292 514h38M292 519h38"/></g>
    <g transform="rotate(-18 734 636)"><ellipse cx="734" cy="636" rx="62" ry="38" fill="#fff" stroke="#f26a1b" stroke-width="3"/></g>
    <g fill="none" stroke="#1d1d1d" stroke-width="2"><path d="M717 624h34l-4 30h-26zM722 630v18M730 630v18M738 630v18M746 630v18"/></g>
  </svg>
  <h2 class="abs svc-h">OUR SERVICES</h2>
  <div class="abs center-name">HAVEN &amp; RESTORE</div>
  <div class="abs svc-item right" style="left:100px;top:1547px;width:275px"><h3>FIRE &amp; SMOKE RESTORATION</h3><p>Sed in dictum sapien. In lacus lacus,<br>malesuada ut arcu et, pellentesque<br>convallis diam.</p></div>
  <div class="abs svc-item" style="left:857px;top:1573px;width:280px"><h3>TESTING SERVICES</h3><p>Sed in dictum sapien. In lacus lacus,<br>malesuada ut arcu et, pellentesque<br>convallis diam.</p></div>
  <div class="abs svc-item right" style="left:40px;top:1882px;width:276px"><h3>WATER RESTORATION</h3><p>Sed in dictum sapien. In lacus lacus,<br>malesuada ut arcu et, pellentesque<br>convallis diam.</p></div>
  <div class="abs svc-item" style="left:816px;top:1905px;width:300px"><h3>HOARDING &amp; SQUALOR CLEANING</h3><p>Sed in dictum sapien. In lacus lacus,<br>malesuada ut arcu et, pellentesque<br>convallis diam.</p></div>
</section>

<section>
  <div class="abs frame-back" style="left:75px;top:2301px;width:444px;height:465px"></div>
  <div class="abs photo-b" role="img" aria-label="Photo of gloved hands dusting a surface with a forensic brush"></div>
  <h2 class="abs crime-h">CRIME SCENE CLEANER</h2>
  <p class="abs lead crime-lead">Haven &amp; Restore Crime and Trauma Scene Decontamination unit offers services in the following areas:</p>
  <ul class="abs checks crime-list">
    <li><svg width="14" height="14" viewBox="0 0 14 14"><circle cx="7" cy="7" r="7" fill="#e2351f"/><path d="M4 7.2l2 2 4-4" stroke="#fff" stroke-width="2" fill="none"/></svg>Trauma cleaning</li>
    <li><svg width="14" height="14" viewBox="0 0 14 14"><circle cx="7" cy="7" r="7" fill="#e2351f"/><path d="M4 7.2l2 2 4-4" stroke="#fff" stroke-width="2" fill="none"/></svg>Blood &amp; tissue clean up</li>
    <li><svg width="14" height="14" viewBox="0 0 14 14"><circle cx="7" cy="7" r="7" fill="#e2351f"/><path d="M4 7.2l2 2 4-4" stroke="#fff" stroke-width="2" fill="none"/></svg>Crime scene cleaning</li>
    <li><svg width="14" height="14" viewBox="0 0 14 14"><circle cx="7" cy="7" r="7" fill="#e2351f"/><path d="M4 7.2l2 2 4-4" stroke="#fff" stroke-width="2" fill="none"/></svg>Death Cleaning</li>
    <li><svg width="14" height="14" viewBox="0 0 14 14"><circle cx="7" cy="7" r="7" fill="#e2351f"/><path d="M4 7.2l2 2 4-4" stroke="#fff" stroke-width="2" fill="none"/></svg>Forensic powder clean up</li>
    <li><svg width="14" height="14" viewBox="0 0 14 14"><circle cx="7" cy="7" r="7" fill="#e2351f"/><path d="M4 7.2l2 2 4-4" stroke="#fff" stroke-width="2" fill="none"/></svg>Suicide Cleaning</li>
  </ul>
  <p class="abs crime-p">Haven &amp; Restore Crime Scene and Trauma Scene Decontamination Unit understand the emotional strain an accident, crime or property neglect can place on a family.<br>When an accident or tragedy strikes, no one is prepared for the emotional and physical toll it can take.</p>
  <a class="abs btn crime-btn">READ MORE</a>
</section>

<section>
  <svg class="abs testi-bg" width="1200" height="600" viewBox="0 0 1200 600">
    <defs><linearGradient id="testiGrad" x1="0" y1="0" x2="0" y2="1"><stop offset="0" stop-color="#e2351f"/><stop offset="1" stop-color="#f47a1e"/></linearGradient></defs>
    <path d="M0 165 C300 30 900 -30 1200 30 L1200 470 C900 590 300 600 0 545 Z" fill="url(#testiGrad)"/>
  </svg>
  <h2 class="abs testi-h">TESTIMONIALS</h2>
  <div class="abs quote" style="left:81px"><div class="q">&rdquo;</div><p>&ldquo; This business has been cleaning our house in chapel hill for 5 years. They are reliable and efficient and we are pleased to recommend their services to others...&rdquo;</p><b>LM - TARINGA</b></div>
  <div class="abs quote" style="left:440px"><div class="q">&rdquo;</div><p>&ldquo; This business has been cleaning our house in chapel hill for 5 years. They are reliable and efficient and we are pleased to recommend their services to others...&rdquo;</p><b>LM - TARINGA</b></div>
  <div class="abs quote" style="left:799px"><div class="q">&rdquo;</div><p>&ldquo; This business has been cleaning our house in chapel hill for 5 years. They are reliable and efficient and we are pleased to recommend their services to others...&rdquo;</p><b>LM - TARINGA</b></div>
  <svg class="abs arrow" style="left:42px" width="16" height="26" viewBox="0 0 16 26"><path d="M13 2L3 13l10 11" stroke="#fff" stroke-width="4" fill="none"/></svg>
  <svg class="abs arrow" style="left:1140px" width="16" height="26" viewBox="0 0 16 26"><path d="M3 2l10 11L3 24" stroke="#fff" stroke-width="4" fill="none"/></svg>
</section>

<section>
  <h2 class="abs touch-h">GET IN TOUCH TODAY</h2>
  <div class="abs touch-c">
    <span><svg width="18" height="18" viewBox="0 0 24 24"><path fill="#e2351f" d="M6.6 10.8a15.1 15.1 0 0 0 6.6 6.6l2.2-2.2c.3-.3.7-.4 1-.2 1.1.4 2.3.6 3.6.6.6 0 1 .4 1 1V20c0 .6-.4 1-1 1A17 17 0 0 1 3 4c0-.6.4-1 1-1h3.5c.6 0 1 .4 1 1 0 1.3.2 2.5.6 3.6.1.3 0 .7-.2 1z"/></svg>1-800-555-0142</span>
    <span><svg width="20" height="16" viewBox="0 0 24 18"><path fill="#e2351f" d="M0 2l12 8 12-8V0H0zm0 3v13h24V5l-12 8z"/></svg>hello@havenrestore.example</span>
  </div>
  <a class="abs btn touch-btn">CONTACT US</a>
</section>

<footer>
  <div class="abs footer"></div>
  <nav class="abs fnav"><a>HOME</a><a>FIRE &amp; SMOKE RESTORATION</a><a>WATER RESTORATION</a><a>CRIME SCENE CLEANERS</a><a>TESTING SERVICES</a><a>HOARDING &amp; SQUALOR CLEANING</a><a>CONTACT US</a></nav>
  <p class="abs copy">Copyright &copy; 2020 Company Name All Rights Reserved</p>
  <div class="abs social"><i></i><i></i><i></i><i></i></div>
</footer>

</body>
</html>
```